I need bigcommerce design template

hi, am looking for a quality, professional, attractive and mature bigcommerce template for my site. My site will sell clothes and bags and shoes. Basically what you are to do is setup the store. I have domain name which hostwren will attach them self.

It Professional

```html
<!DOCTYPE html>
<html lang="en">
<head>
<meta charset="utf-8">
<title>Storefront Home</title>
<link href="https://fonts.googleapis.com/css2?family=Roboto:wght@300;400;500;700;900&family=Oswald:wght@500;700&display=swap" rel="stylesheet">
<style>
:root{
  --accent:#e8562a;
  --dark:#1c1c1c;
  --ink:#333;
  --muted:#8a8a8a;
  --line:#e3e3e3;
  --band:#f2f2f2;
  --star:#f39c12;
  --white:#fff;
}
*{box-sizing:border-box;margin:0;padding:0}
html,body{width:1200px;height:2524px;overflow:hidden;background:var(--white);font-family:"Roboto",sans-serif;color:var(--ink)}
.page{position:relative;width:1200px;height:2524px}
.wrap{position:absolute;left:120px;width:960px}
a{color:inherit;text-decoration:none}

.topbar{position:absolute;top:0;left:0;width:1200px;height:30px;background:var(--dark);color:#bbb;font-size:11px}
.topbar .wrap{top:0;height:30px;display:flex;align-items:center;justify-content:space-between}
.topbar span{margin-right:14px}

.header .wrap{top:42px;height:44px;display:flex;align-items:center;justify-content:space-between}
.brand{display:flex;align-items:center;gap:10px;font-size:34px;font-weight:700;color:var(--ink);letter-spacing:1px}
.brand i{width:22px;height:22px;background:var(--accent);display:block}
.search{width:230px;height:30px;border:1px solid var(--line);font-size:12px;color:var(--muted);display:flex;align-items:center;justify-content:space-between;padding:0 10px}

.nav{position:absolute;top:96px;left:120px;width:960px;height:32px;border-bottom:1px solid var(--line);display:flex;align-items:center;font-size:12px;font-weight:500}
.nav a{margin-right:30px;height:32px;line-height:32px}
.nav a.on{color:var(--accent);border-bottom:2px solid var(--accent)}
.nav .cart{margin-left:auto;color:var(--accent);display:flex;align-items:center;gap:6px}

.hero{top:138px;height:400px}
.slide{position:absolute;left:0;top:0;width:720px;height:400px;background:linear-gradient(90deg,#c98a55,#dcae80 55%,#c4915f)}
.slide .photo{position:absolute;right:40px;top:0;width:330px;height:400px;background:linear-gradient(180deg,#b27a4a,#8f5a34)}
.slide .tag{position:absolute;left:60px;top:62px;font-size:13px;font-weight:700;color:var(--white);background:var(--accent);padding:4px 8px}
.slide h1{position:absolute;left:60px;top:100px;font-family:"Oswald",sans-serif;font-size:46px;line-height:52px;color:var(--white);text-transform:uppercase}
.slide .btn{position:absolute;left:60px;top:236px;background:var(--accent);color:var(--white);font-size:13px;padding:11px 20px}
.arrow{position:absolute;top:186px;width:28px;height:28px}
.side{position:absolute;left:732px;width:228px;height:194px}
.side.a{top:0;background:linear-gradient(160deg,#6a6a6a,#2f2f2f)}
.side.b{top:206px;background:linear-gradient(160deg,#7a3c2c,#3a2219)}
.side span{position:absolute;color:var(--white);font-weight:700;font-size:18px;line-height:22px}

.section-title{position:absolute;left:120px;width:960px;font-size:13px;font-weight:700;text-transform:uppercase;border-bottom:1px solid var(--line);padding-bottom:8px;display:flex;justify-content:space-between}
.section-title .pager{display:flex;gap:4px}
.section-title .pager i{width:16px;height:16px;border:1px solid var(--line);display:block}

.products{top:596px;height:300px;display:flex;justify-content:space-between}
.card{width:148px;text-align:center;position:relative}
.card .pic{height:176px;border:1px solid var(--line);display:flex;align-items:center;justify-content:center}
.card .pic div{width:90px;height:160px;border-radius:40px 40px 6px 6px}
.card .sale{position:absolute;top:-8px;right:6px;width:34px;height:34px;border-radius:50%;background:var(--dark);color:var(--white);font-size:10px;line-height:34px;font-weight:700}
.card small{display:block;font-size:9px;color:var(--muted);margin-top:8px;text-transform:uppercase}
.card h3{font-size:12px;font-weight:500;margin-top:2px}
.stars{color:var(--star);font-size:13px;letter-spacing:1px;margin-top:2px}
.price{color:var(--accent);font-size:12px;font-weight:700;margin-top:2px}
.price s{color:var(--muted);font-weight:400;margin-right:4px}
.card .opt{display:inline-block;margin-top:8px;font-size:9px;border:1px solid var(--line);padding:5px 10px;color:var(--muted)}

.cats{top:1028px;height:472px}
.cat{position:absolute;color:var(--white);font-weight:700}
.cat span{position:absolute;font-size:20px;text-shadow:0 1px 3px rgba(0,0,0,.4)}
.cat.men{left:0;top:0;width:472px;height:472px;background:linear-gradient(135deg,#8d8d8d,#3b3b3b 70%)}
.cat.women{left:492px;top:0;width:468px;height:226px;background:linear-gradient(120deg,#bfb2a3,#6e5a48)}
.cat.tees{left:492px;top:246px;width:224px;height:226px;background:linear-gradient(160deg,#5b6b74,#2a3237)}
.cat.casual{left:736px;top:246px;width:224px;height:226px;background:linear-gradient(160deg,#8a3a28,#3a1a12)}

.blog{top:1590px;height:180px;display:flex;justify-content:space-between}
.post{width:300px}
.post .pic{height:110px;position:relative}
.post .date{position:absolute;left:10px;top:10px;width:34px;height:40px;background:var(--dark);color:var(--white);font-size:10px;text-align:center;line-height:14px;padding-top:5px}
.post h4{color:var(--accent);font-size:12px;margin-top:12px;font-weight:500}
.post p{font-size:10px;color:var(--muted);line-height:14px;margin-top:4px}
.post em{display:block;font-style:normal;font-size:9px;color:var(--muted);margin-top:6px}

.band{position:absolute;top:1808px;left:0;width:1200px;height:372px;background:var(--band)}
.cols{top:1830px;height:330px;display:flex;gap:30px}
.col{width:217px}
.col h5{font-size:11px;font-weight:700;text-transform:uppercase;padding-bottom:8px;border-bottom:1px solid #d9d9d9;margin-bottom:12px}
.mini{display:flex;gap:10px;margin-bottom:14px}
.mini .thumb{width:44px;height:56px;background:#ddd;border:1px solid #d0d0d0}
.mini b{display:block;font-size:11px;font-weight:500}
.mini .stars{font-size:10px}
.mini .price{font-size:10px}
.feed{background:var(--white);border:1px solid #d9d9d9;height:210px;padding:8px;font-size:10px}
.feed .row{display:flex;gap:6px;margin-top:8px}
.feed .row i{width:30px;height:30px;background:#c7d3dc;display:block;flex:none}
.feed .shot{height:70px;margin-top:8px;background:linear-gradient(135deg,#6aa0c8,#2e5f86)}
.feature{height:260px;background:linear-gradient(160deg,#9b8f86,#403630)}

.footer{position:absolute;top:2208px;left:0;width:1200px;height:316px;background:var(--dark);color:#aaa;font-size:11px}
.fcols{top:28px;height:220px;display:flex;gap:30px}
.fcols .brand{color:var(--white);font-size:28px}
.fcol h6{color:var(--white);font-size:11px;text-transform:uppercase;margin-bottom:12px}
.fcol p,.fcol li{line-height:18px;list-style:none}
.links{display:flex;gap:36px}
.links li{color:var(--accent)}
.social{display:flex;gap:6px;margin-bottom:16px}
.social i{width:22px;height:22px;border-radius:50%;background:var(--accent);display:block}
.signup{display:flex}
.signup div{width:170px;height:28px;background:var(--white)}
.signup span{background:var(--accent);color:var(--white);font-size:10px;line-height:28px;padding:0 10px;font-weight:700}
.bottom{position:absolute;left:0;bottom:0;width:1200px;height:40px;border-top:1px solid #333;font-size:10px}
.bottom .wrap{top:0;height:40px;display:flex;align-items:center}
</style>
</head>
<body>
<div class="page">

  <div class="topbar"><div class="wrap">
    <div><span>USD $</span><span>EN</span><span>Help</span><span>FAQ</span></div>
    <div><span>Sign in</span><span>My Account</span></div>
  </div></div>

  <header class="header"><div class="wrap">
    <a class="brand" href="#"><i></i>LOGO</a>
    <div class="search"><span>Product Search</span>
      <svg width="12" height="12" viewBox="0 0 12 12"><circle cx="5" cy="5" r="4" fill="none" stroke="#999" stroke-width="1.5"/><line x1="8" y1="8" x2="11" y2="11" stroke="#999" stroke-width="1.5"/></svg>
    </div>
  </div></header>

  <nav class="nav">
    <a class="on" href="#">HOME</a><a href="#">SHOP ▾</a><a href="#">BLOG ▾</a><a href="#">SHOWCASE ▾</a><a href="#">SHORTCODES ▾</a><a href="#">PAGES ▾</a>
    <span class="cart"><svg width="16" height="14" viewBox="0 0 16 14"><path d="M1 1h3l2 8h8l1-6H5" fill="none" stroke="#e8562a" stroke-width="1.5"/><circle cx="7" cy="12" r="1.3" fill="#e8562a"/><circle cx="13" cy="12" r="1.3" fill="#e8562a"/></svg>$0.00</span>
  </nav>

  <section class="wrap hero">
    <div class="slide">
      <div class="photo" role="img" aria-label="Young man in glasses and bow tie wearing a brown jacket"></div>
      <span class="tag">SALE NOW ON!</span>
      <h1>Mens Fashion<br>Get Stylish!</h1>
      <a class="btn" href="#">Read More</a>
      <svg class="arrow" style="left:10px" viewBox="0 0 28 28"><path d="M17 7l-7 7 7 7" fill="none" stroke="#fff" stroke-width="2.5"/></svg>
      <svg class="arrow" style="right:10px" viewBox="0 0 28 28"><path d="M11 7l7 7-7 7" fill="none" stroke="#fff" stroke-width="2.5"/></svg>
    </div>
    <div class="side a" role="img" aria-label="Woman in a black outfit, sale banner"><span style="right:14px;top:20px;text-align:right">50% off<br>sale!</span></div>
    <div class="side b" role="img" aria-label="Casual autumn clothing banner"><span style="left:14px;top:80px">Autumn<br>Collection</span></div>
  </section>

  <div class="section-title" style="top:566px"><span>Latest Products</span><span class="pager"><i></i><i></i></span></div>
  <section class="wrap products">
    <div class="card"><div class="pic" role="img" aria-label="Pink hooded top"><div style="background:#c2457f"></div></div><small>Hoodies</small><h3>Elevate Hoodie</h3><div class="stars">★★★★★</div><div class="price">$79.00</div><span class="opt">CHOOSE OPTIONS</span></div>
    <div class="card"><div class="pic" role="img" aria-label="Light pink tee"><div style="background:#efa3b5"></div></div><small>T-Shirts</small><h3>Feather Tee</h3><div class="stars">★★★★★</div><div class="price">$29.00</div><span class="opt">ADD TO CART</span></div>
    <div class="card"><span class="sale">SALE</span><div class="pic" role="img" aria-label="Black wool coat"><div style="background:#222"></div></div><small>Jackets</small><h3>Woolen Jacket</h3><div class="stars">★★★★★</div><div class="price"><s>$59.00</s>$45.00</div><span class="opt">CHOOSE OPTIONS</span></div>
    <div class="card"><div class="pic" role="img" aria-label="Grey long sleeve top"><div style="background:#7d8791"></div></div><small>Tops</small><h3>Striped Top</h3><div class="stars">★★★★★</div><div class="price">$39.00</div><span class="opt">ADD TO CART</span></div>
    <div class="card"><div class="pic" role="img" aria-label="Navy hooded sweatshirt"><div style="background:#2f3c55"></div></div><small>Hoodies</small><h3>Redford</h3><div class="stars">★★★★★</div><div class="price">$49.00</div><span class="opt">CHOOSE OPTIONS</span></div>
  </section>

  <section class="wrap cats">
    <a class="cat men" href="#" role="img" aria-label="Man in a dark suit"><span style="left:150px;top:230px">Men's Clothing</span></a>
    <a class="cat women" href="#" role="img" aria-label="Woman in a hat outdoors"><span style="left:190px;top:90px">Women's Clothing</span></a>
    <a class="cat tees" href="#" role="img" aria-label="Stacked t-shirts"><span style="left:40px;top:90px">T-Shirts<br>&amp; Tops</span></a>
    <a class="cat casual" href="#" role="img" aria-label="Casual jackets"><span style="left:110px;top:90px">Casual<br>Jackets</span></a>
  </section>

  <div class="section-title" style="top:1540px"><span>From the Blog</span><span class="pager"><i></i></span></div>
  <section class="wrap blog">
    <article class="post"><div class="pic" role="img" aria-label="Row of colourful shirts" style="background:linear-gradient(90deg,#c9b59c,#7c8fa6)"><span class="date">08<br>JUN</span></div><h4>Stand out from the crowd!</h4><p>Fresh looks for every season, picked by our team to help you build a wardrobe that feels like you.</p><em>2 comments</em></article>
    <article class="post"><div class="pic" role="img" aria-label="Plate of healthy food" style="background:linear-gradient(90deg,#b98656,#5a3b24)"><span class="date">06<br>JUN</span></div><h4>Our Latest Podcast – Healthy Eating</h4><p>Simple habits for busy days, quick recipes and tips to keep your energy up from morning to night.</p><em>3 comments</em></article>
    <article class="post"><div class="pic" role="img" aria-label="Road trip scene" style="background:linear-gradient(90deg,#d29a6a,#6f4a38)"><span class="date">02<br>JUN</span></div><h4>Mara Levin, On the Road</h4><p>Notes from a long drive west, with the pieces we packed and the places that made the trip worth it.</p><em>5 comments</em></article>
  </section>

  <div class="band"></div>
  <section class="wrap cols">
    <div class="col"><h5>Recent Reviews</h5>
      <div class="mini"><div class="thumb" role="img" aria-label="Hoodie thumbnail"></div><div><b>Elevate Hoodie</b><div class="stars">★★★★★</div><div class="price">$79.00</div></div></div>
      <div class="mini"><div class="thumb" role="img" aria-label="Tee thumbnail"></div><div><b>Feather Tee</b><div class="stars">★★★★★</div><div class="price">$29.00</div></div></div>
      <div class="mini"><div class="thumb" role="img" aria-label="Sunglasses thumbnail"></div><div><b>Sunglasses Frames</b><div class="stars">★★★★★</div><div class="price">$19.00</div></div></div>
    </div>
    <div class="col"><h5>Popular</h5>
      <div class="mini"><div class="thumb" role="img" aria-label="Hoodie thumbnail"></div><div><b>Elevate Hoodie</b><div class="stars">★★★★★</div><div class="price">$79.00</div></div></div>
      <div class="mini"><div class="thumb" role="img" aria-label="Tee thumbnail"></div><div><b>Feather Tee</b><div class="stars">★★★★★</div><div class="price">$29.00</div></div></div>
      <div class="mini"><div class="thumb" role="img" aria-label="Jacket thumbnail"></div><div><b>Field Jacket</b><div class="stars">★★★★★</div><div class="price">$89.00</div></div></div>
    </div>
    <div class="col"><h5>Chirpline</h5>
      <div class="feed"><b>Posts</b>
        <div class="row"><i></i><span>New arrivals are in store now, come see the autumn line.</span></div>
        <div class="shot" role="img" aria-label="Shared photo in feed"></div>
        <div class="row"><i></i><span>Free shipping on all orders this weekend.</span></div>
      </div>
    </div>
    <div class="col"><h5>Feature</h5><div class="feature" role="img" aria-label="Seasonal collection feature photo"></div></div>
  </section>

  <footer class="footer">
    <div class="wrap fcols">
      <div class="fcol" style="width:230px"><a class="brand" href="#"><i></i>LOGO</a><p style="margin-top:14px">14 Harbour Lane<br>Westbrook, CA 90011<br>United States<br>hello@northvale.shop<br>+1 555 0142</p></div>
      <div class="fcol" style="width:230px"><h6>Browse</h6><div class="links"><ul><li>Men</li><li>Women</li><li>Shoes</li><li>Bags</li><li>Accessories</li></ul><ul><li>About Us</li><li>Contact</li><li>Blog</li><li>Shipping</li><li>Returns</li></ul></div></div>
      <div class="fcol" style="width:230px"><h6>About Northvale</h6><p>Quality clothing, bags and shoes chosen with care. Built to last, styled for everyday wear and made to feel good.</p></div>
      <div class="fcol" style="width:210px"><h6>Connect With Us</h6><div class="social"><i></i><i></i><i></i><i></i><i></i><i></i></div><h6>Newsletter Signup</h6><div class="signup"><div></div><span>SIGN UP</span></div></div>
    </div>
    <div class="bottom"><div class="wrap">© 2015 Copyright Northvale. All rights reserved.</div></div>
  </footer>

</div>
</body>
</html>
```